Website Home Page Main Banner Design (wholesale)

1170 x 547 PNG web banner design

Verano Global Corporation is a full-service importer based out of New York City, New York. For over 50 years, we have offered our customers fashionable, quality products at competitive prices. The company has a full in-house development and design staff, with a 100,000 sq. foot warehouse in Perth Amboy, New Jersey. Our talented design team, with extensive overseas sourcing experience, is always on the search for innovative ideas and hot new products.

Verano currently consists of the following divisions– Toddler Novelty Company (TNC), Hair Accessories, Jewelry (Gleamora), General Merchandise (Brandavex), Beauty Implements, Socks & Hosiery and Electronics.

Website- https://verano.quillbrook-hosting.com/index.php/

Target Market(s)

Retailers

Industry/Entity Type

Wholesale

Number of Pages Required

1 page

Font styles to use
Serif

Colors

Designer to choose colors to be used in the design.

Requirements
Must have
• Company Name- Verano Global Corp
Nice to have
• Some of the products featured on the site
Should not have
• Nothing

```html
<!DOCTYPE html>
<html lang="en">
<head>
<meta charset="utf-8">
<title>Verano Global Corp – Home Banner</title>
<link rel="stylesheet" href="https://fonts.googleapis.com/css2?family=Lato:wght@400;700&family=Raleway:wght@300;400&family=Playball&display=swap">
<style>
  :root {
    --paper-light: #fbfbfb;
    --paper-mid: #ececec;
    --ink: #333333;
    --ink-soft: #6e6e6e;
    --lavender: #a99be6;
    --nav-pink: #ec82c0;
    --rule: #cfcfcf;
    --sep: #8a8a8a;
    --hat-pink: #f06fa0;
    --hat-light: #f8a3c3;
    --bootie-pink: #f5a2c1;
    --bootie-light: #fcd6e4;
    --card-black: #2b2b2b;
    --jewel-silver: #b9b9b9;
    --jewel-dark: #3a3a3a;
    --comb-black: #1f1f1f;
    --comb-red: #d63a55;
    --sock-green: #58b466;
    --sock-dark: #2a2a2a;
    --bag-green: #5ea634;
    --bag-light: #86c555;
    --bag-magenta: #c8327f;
  }
  html, body { margin: 0; padding: 0; overflow: hidden; }
  .banner {
    position: relative;
    width: 1200px;
    height: 561px;
    overflow: hidden;
    background: radial-gradient(ellipse at 50% 45%, var(--paper-light) 0%, var(--paper-mid) 100%);
    font-family: "Lato", sans-serif;
    color: var(--ink);
  }

  /* Brand */
  .brand {
    position: absolute;
    left: 0; right: 0;
    top: 76px;
    text-align: center;
  }
  .brand-name {
    display: inline-flex;
    align-items: center;
    gap: 12px;
    font-family: "Raleway", sans-serif;
    font-weight: 400;
    font-size: 34px;
    line-height: 40px;
    color: var(--lavender);
  }
  .brand-square { width: 22px; height: 22px; background: var(--lavender); }
  .founded {
    position: absolute;
    left: 0; right: 0;
    top: 178px;
    text-align: center;
    font-size: 15px;
    line-height: 18px;
    letter-spacing: 0.3px;
    color: var(--ink);
  }

  /* Tagline */
  .tagline {
    position: absolute;
    left: 499px;
    top: 233px;
    width: 202px;
    text-align: center;
    font-family: "Raleway", sans-serif;
    font-weight: 300;
    white-space: nowrap;
  }
  .tagline .ruled {
    display: flex;
    align-items: center;
    gap: 12px;
    height: 20px;
    font-size: 16px;
    color: var(--ink);
  }
  .tagline .ruled::before,
  .tagline .ruled::after {
    content: "";
    flex: 1;
    height: 1px;
    background: var(--ink);
  }
  .tagline .ruled-in { font-size: 13px; }
  .tagline .one-stop {
    font-size: 22px;
    line-height: 28px;
    color: var(--ink-soft);
  }
  .tagline .script {
    font-family: "Playball", cursive;
    font-size: 37px;
    line-height: 42px;
    color: #222222;
  }
  .tagline .fashion {
    font-size: 29px;
    line-height: 38px;
    color: #2a2a2a;
  }
  .tagline .industry {
    font-size: 16.5px;
    line-height: 24px;
    color: var(--ink-soft);
  }

  /* Product areas */
  .product { position: absolute; }
  .product-hat {
    left: 18px; top: 238px; width: 136px; height: 111px;
    border-radius: 48% 48% 38% 38%;
    background: radial-gradient(circle at 62% 45%, var(--hat-light) 0%, var(--hat-pink) 75%);
  }
  .product-booties {
    left: 159px; top: 272px; width: 126px; height: 92px;
    border-radius: 18px 18px 10px 10px;
    background: linear-gradient(180deg, var(--bootie-light) 0%, var(--bootie-pink) 100%);
  }
  .product-earrings {
    left: 321px; top: 208px; width: 108px; height: 202px;
    border-radius: 4px;
    background: linear-gradient(180deg, var(--card-black) 0%, var(--card-black) 27%, var(--jewel-silver) 27%, var(--jewel-dark) 100%);
  }
  .product-combs {
    left: 754px; top: 242px; width: 126px; height: 117px;
    border-radius: 3px;
    background: linear-gradient(90deg, var(--comb-black) 0%, var(--comb-black) 24%, var(--comb-red) 24%, var(--comb-red) 46%, var(--comb-black) 46%, #3a3a3a 100%);
  }
  .product-socks {
    left: 903px; top: 241px; width: 141px; height: 118px;
    border-radius: 8px;
    background: linear-gradient(90deg, #f2f2f2 0%, var(--sock-dark) 38%, var(--sock-green) 52%, var(--sock-green) 72%, var(--sock-dark) 100%);
  }
  .product-gift-bag {
    left: 1054px; top: 218px; width: 136px; height: 165px;
    border-radius: 2px;
    background: linear-gradient(165deg, var(--bag-green) 0%, var(--bag-light) 60%, var(--bag-magenta) 100%);
  }

  /* Division navigation */
  .divisions {
    position: absolute;
    left: 67px;
    top: 464px;
    width: 1066px;
    height: 32px;
    border-top: 1px solid var(--rule);
    border-bottom: 1px solid var(--rule);
    display: flex;
    justify-content: center;
    align-items: center;
    gap: 17px;
    font-size: 16px;
    color: var(--nav-pink);
    white-space: nowrap;
  }
  .divisions .sep { color: var(--sep); }
</style>
</head>
<body>
  <div class="banner">
    <div class="brand">
      <span class="brand-name"><span class="brand-square"></span>Verano Global Corp</span>
    </div>
    <div class="founded">FOUNDED IN 1961</div>

    <div class="product product-hat" role="img" aria-label="Pink crochet infant hat with a flower"></div>
    <div class="product product-booties" role="img" aria-label="Pair of pink ruffled infant booties"></div>
    <div class="product product-earrings" role="img" aria-label="Silver and black hoop earrings on a black display card"></div>

    <div class="tagline">
      <div class="ruled">THE</div>
      <div class="one-stop">ONE-STOP-SHOP</div>
      <div class="script">for Retailers</div>
      <div class="ruled ruled-in">IN</div>
      <div class="fashion">THE FASHION</div>
      <div class="industry">ACCESSORY INDUSTRY</div>
    </div>

    <div class="product product-combs" role="img" aria-label="Set of black and red hair combs on cards"></div>
    <div class="product product-socks" role="img" aria-label="Pair of striped novelty socks"></div>
    <div class="product product-gift-bag" role="img" aria-label="Green happy birthday gift bag with a cupcake"></div>

    <nav class="divisions">
      <span>INFANT SPECIALTY</span><span class="sep">|</span>
      <span>HAIR ACCESSORIES</span><span class="sep">|</span>
      <span>JEWELRY</span><span class="sep">|</span>
      <span>SOCKS</span><span class="sep">|</span>
      <span>HBA</span><span class="sep">|</span>
      <span>GENERAL MERCHANDISE</span>
    </nav>
  </div>
</body>
</html>
```